Website Comps for Famous Southern BBQ Restaurant in Alabama

We need an authentic, brand-focused redesign for a restaurant.

We need an authentic look.
The client really likes this website.
https://pelzerpit.com/

I don't want to see a bunch of crazy colors.
Avoid image sliders on the homepage. I hate those.

Please mockup the following three pages:
Homepage
Interior page (for mockup purposes, you can do an About page)
Menu page

I only need the PSD's; not the website coded.

Here is the current website: www.dunmoresmokehouse.com

https://pelzerpit.com/

Here are some additional stock photos. New photos will be shot, but these may help for your mock-up designs.
https://www.filecrate.net/sh/83kqvtrpe21zwa9/QXM71bTr4-plWnfVoe8KtYjd?dl=0
Updates

I realize we don't have a lot of high-quality photos to work with.Those will be shot.Here are some additional stock photos that may help.https://www.filecrate.net/sh/83kqvtrpe21zwa9/QXM71bTr4-plWnfVoe8KtYjd?dl=0 Added Saturday, June 10, 2017

Target Market(s)

United states

Industry/Entity Type

Restaurant

Number of Pages Required

3 page

Font styles to use
Sans Serif

Colors

Designer to choose colors to be used in the design.

Requirements
Must have
• An authentic look.
• The client really likes this website.
• https://pelzerpit.com/
• It's simple, bold, and vintage at the same time.
• That is what we want.
• Our existing website is
• dunmoresmokehouse.com
Nice to have
• Simplicity. Something that makes the food look good.
• Possibly a background.
• Logo:
• https://www.filecrate.net/s/k58tnwpl3ovza2e/dunmore-smokehouse-ridgeway.png?dl=0
• Here is a sampling of photos for your comps:
• https://www.filecrate.net/sh/61vbqzhoewpxtn4/QLT4b8JKyRmPPwf6c2ZnHUVpe?dl=0
Should not have
• Nothing too busy.
• Not too many colors.
• Keep it simple, authentic, "down home."
• No homepage image sliders.

```html
<!DOCTYPE html>
<html lang="en">
<head>
<meta charset="utf-8">
<title>Dunmore Smokehouse — Homepage</title>
<link href="https://fonts.googleapis.com/css2?family=Oswald:wght@300;500;700&family=Lato:wght@400;700&display=swap" rel="stylesheet">
<style>
:root{
  --brown:#5a1c0c;
  --orange:#f39c12;
  --orange-deep:#e8890c;
  --ink:#2b2b2b;
  --muted:#777;
  --dark:#151515;
  --panel:#1e1e1e;
  --white:#fff;
}
*{margin:0;padding:0;box-sizing:border-box}
html,body{width:1200px;height:1200px;overflow:hidden;background:#fff}
body{font-family:'Lato',sans-serif;color:var(--ink)}
.stage{position:absolute;left:0;top:0;width:1500px;height:1500px;transform:scale(.8);transform-origin:0 0}
.page{position:absolute;left:537px;top:0;width:425px;height:1500px;background:#fff;overflow:hidden}
.abs{position:absolute}
.photo{position:absolute}
.title{font-family:'Oswald',sans-serif;font-weight:700;color:var(--orange);text-align:center;letter-spacing:.3px;position:absolute;left:0;width:425px}
.sub{position:absolute;left:0;width:425px;text-align:center;font-size:4.4px}
.rule{position:absolute;left:187px;width:52px;height:1px;background:#999}
.tiny{font-size:3.4px;line-height:5.6px;color:var(--muted)}

/* top bar + nav */
.topbar{top:0;left:0;width:425px;height:12px;background:var(--brown)}
.topbar .welcome{position:absolute;left:54px;top:3.5px;font-size:3.6px;color:#fff}
.topbar .welcome b{color:var(--orange)}
.social{position:absolute;top:2.5px;width:6px;height:6px;border-radius:50%;border:.6px solid var(--orange)}
.nav{top:12px;left:0;width:425px;height:28px;background:#fff}
.nav a{position:absolute;top:12.5px;font-size:3.5px;font-weight:700;color:#333;text-decoration:none;letter-spacing:.2px}
.brand{left:186px;top:0;width:54px;height:56px;background:var(--brown);border-bottom:2px solid var(--orange);z-index:3;display:flex;align-items:center;justify-content:center;text-align:center}
.brand span{font-family:'Oswald',sans-serif;font-weight:700;font-size:8px;line-height:9px;color:var(--orange);text-transform:uppercase}

/* hero */
.hero{top:40px;left:0;width:425px;height:178px;background:radial-gradient(ellipse at 50% 85%,#7a3510 0%,#3a2418 35%,#1c2430 70%,#121a24 100%)}
.hero-box{left:91px;top:48px;width:243px;height:102px;background:rgba(0,0,0,.7);text-align:center}
.hero-box .pre{font-family:'Oswald',sans-serif;font-weight:300;color:var(--orange);font-size:15px;margin-top:8px}
.hero-box h1{font-family:'Oswald',sans-serif;font-weight:500;color:#fff;font-size:24px;line-height:26px}
.hero-box p{font-size:4.2px;color:var(--orange);line-height:6px;margin-top:4px}
.hero-btn{left:188px;top:129px;width:49px;height:14px;border:1px solid #bbb;border-radius:8px;background:rgba(0,0,0,.5);color:#fff;font-size:3.4px;text-align:center;line-height:12px}

/* about */
.story-img{left:53px;top:300px;width:148px;height:103px;border:3px solid #eee;background:linear-gradient(135deg,#6b4a34,#3c2f24 45%,#c9c3ba 75%,#8a6e58)}
.story h3{position:absolute;left:213px;top:306px;font-family:'Oswald',sans-serif;font-weight:500;font-size:8px;color:var(--brown)}
.story p{position:absolute;left:213px;width:160px;font-size:3.3px;line-height:5.8px;color:#666;font-style:italic}

/* dark sections */
.band{left:0;width:425px;background:linear-gradient(180deg,#1a1a1a,#2a2a2a 50%,#151515)}
.band .sub{color:#fff}
.offer-card{position:absolute;top:496px;width:76px;height:80px;border:2px solid #fff}
.offer-tag{position:absolute;top:558px;width:62px;height:31px;background:#fff;text-align:center}
.offer-tag .name{font-size:4.2px;color:#333;margin-top:5px}
.offer-tag .price{position:absolute;left:5px;top:14px;font-family:'Oswald',sans-serif;font-weight:700;font-size:8px;color:var(--brown)}
.offer-tag .stars{position:absolute;left:26px;top:16px;font-size:4px;color:var(--orange);letter-spacing:.3px}

/* gallery */
.filters{position:absolute;top:696px;left:0;width:425px;text-align:center;font-size:4.2px;color:#777}
.filters span{margin:0 3px}
.filters .on{color:var(--orange)}

/* chefs */
.chef{position:absolute;top:930px;width:69px;height:70px;border:2px solid #eee}
.chef-cap{position:absolute;top:1011px;width:80px;text-align:center}
.chef-cap b{display:block;font-family:'Oswald',sans-serif;font-size:4.6px;color:var(--brown);font-weight:700}
.chef-cap i{display:block;font-style:normal;font-size:4px;color:var(--orange);margin-top:2px}
.chef-cap span{display:block;font-size:3.2px;line-height:5px;color:#777;margin-top:2px}

/* reservations */
.form-label{left:53px;top:1113px;font-family:'Oswald',sans-serif;font-weight:500;font-size:6.6px;color:#fff}
.field{position:absolute;height:13px;border:.8px solid #888;background:rgba(0,0,0,.35);font-size:3.4px;color:#aaa;padding:4px 5px}
.field svg{position:absolute;right:4px;top:3.5px}
.res-note{left:53px;top:1188px;font-size:4px;color:#ddd}
.res-btn{left:321px;top:1183px;width:51px;height:15px;background:var(--orange-deep);color:#fff;font-size:3.4px;font-weight:700;text-align:center;line-height:15px}

/* blog */
.post-img{position:absolute;top:1296px;width:76px;height:59px}
.post{position:absolute;top:1295px;width:78px}
.post h4{font-family:'Oswald',sans-serif;font-weight:700;font-size:4.6px;color:var(--brown)}
.post .meta{font-size:3.2px;color:#aaa;margin:3px 0}
.post p{font-size:3.2px;line-height:5.4px;color:#666}
.post .more{font-size:3.4px;color:var(--orange);font-weight:700;margin-top:3px}

/* footer */
.footer{top:1373px;left:0;width:425px;height:127px;background:var(--dark)}
.footer h5{position:absolute;top:1398px;font-family:'Oswald',sans-serif;font-weight:500;font-size:7px;color:var(--orange)}
.foot-brand{left:53px;top:1398px;width:25px;height:23px;background:var(--brown);color:var(--orange);font-family:'Oswald',sans-serif;font-weight:700;font-size:3.6px;text-align:center;padding-top:6px;line-height:5px}
.foot-txt{font-size:3.4px;line-height:5.6px;color:#ccc}
.foot-txt b{color:var(--orange)}
.thumb{position:absolute;width:16px;height:15px}
.copy{top:1483px;left:0;width:425px;height:17px;border-top:.6px solid #333;text-align:center;font-size:3px;color:#888;padding-top:6px}
</style>
</head>
<body>
<div class="stage">
<main class="page">

  <header>
    <div class="abs topbar">
      <div class="welcome">Welcome to <b>Dunmore Smokehouse</b></div>
      <span class="social" style="left:337px"></span>
      <span class="social" style="left:346px"></span>
      <span class="social" style="left:355px"></span>
      <span class="social" style="left:364px"></span>
    </div>
    <nav class="abs nav">
      <a style="left:54px">HOME</a>
      <a style="left:75px">ABOUT</a>
      <a style="left:98px">LOCATIONS</a>
      <a style="left:129px">RESTAURANT MENUS</a>
      <a style="left:268px">CATERING</a>
      <a style="left:300px">NEWS</a>
      <a style="left:324px">STORE</a>
      <a style="left:351px">CONTACT US</a>
    </nav>
    <div class="abs brand"><span>Dunmore<br>Smokehouse</span></div>
  </header>

  <section class="abs hero" role="img" aria-label="Meat grilling over glowing coals with smoke rising">
    <div class="abs hero-box">
      <div class="pre">GOOD FOOD IS</div>
      <h1>GOOD MOOD</h1>
      <p>Cras tincidunt elit mattis rhoncus faucibus. Mauris egestas mi elit. Donec pretium,<br>enim non sollicitudin congue, dolor turpis faucibus libero.</p>
    </div>
    <div class="abs hero-btn">VIEW ALL STORE</div>
  </section>

  <section class="about">
    <h2 class="title" style="top:245px;font-size:12px">ABOUT US</h2>
    <p class="sub" style="top:264px;color:#666;line-height:6.4px">Cras tincidunt elit mattis rhoncus faucibus. Mauris egestas mi elit. Donec pretium,<br>enim non sollicitudin congue, dolor turpis faucibus libero.</p>
    <div class="photo story-img" role="img" aria-label="Bowl of collard greens with bread and a plate of barbecue"></div>
    <div class="story">
      <h3>OUR STORY</h3>
      <p style="top:321px">Our pit has been smoking low and slow since the early days. Every rack is rubbed by hand and<br>cooked over hickory until the bark is just right for the table.</p>
      <p style="top:339px">Our pit has been smoking low and slow since the early days. Every rack is rubbed by hand and<br>cooked over hickory until the bark is just right for the table.</p>
      <p style="top:356px">Sauce recipes came down through the family, and we still mix them in small batches each<br>morning so every plate tastes the way it did when we first opened<br>our doors to the town.</p>
      <p style="top:381px">Come hungry, sit a while and bring the whole family along for sweet tea, good<br>company and a plate piled high. Seats open daily.</p>
    </div>
  </section>

  <section class="abs band" style="top:425px;height:191px">
    <h2 class="title" style="top:20px;font-size:12px">OUR SPECIAL OFFER</h2>
    <p class="sub" style="top:37px">Praesent Rutrum Pretium Urna</p>
    <div class="rule" style="top:50px"></div>
  </section>
  <div class="offer-card photo" style="left:53px;background:linear-gradient(160deg,#b07a3a,#5a3a20 60%,#eee)" role="img" aria-label="Burger with lettuce and tomato"></div>
  <div class="offer-card photo" style="left:134px;background:linear-gradient(160deg,#4a3a30,#d8cfc6 55%,#6b4d38)" role="img" aria-label="Chocolate dessert plated"></div>
  <div class="offer-card photo" style="left:215px;background:linear-gradient(160deg,#6a2a18,#e07040 55%,#f0c080)" role="img" aria-label="Glasses of iced fruit drinks"></div>
  <div class="offer-card photo" style="left:296px;background:linear-gradient(160deg,#f4f2ee,#e8e4dc 55%,#d89840)" role="img" aria-label="Plate of pasta with shrimp"></div>
  <div class="offer-tag" style="left:60px"><div class="name">QUIS ANTE</div><div class="price">20$</div><div class="stars">★★★★☆</div></div>
  <div class="offer-tag" style="left:141px"><div class="name">QUIS ANTE</div><div class="price">20$</div><div class="stars">★★★★☆</div></div>
  <div class="offer-tag" style="left:222px"><div class="name">QUIS ANTE</div><div class="price">20$</div><div class="stars">★★★★☆</div></div>
  <div class="offer-tag" style="left:303px"><div class="name">QUIS ANTE</div><div class="price">20$</div><div class="stars">★★★★☆</div></div>

  <section class="gallery">
    <h2 class="title" style="top:645px;font-size:12px">FOOD GALLERY</h2>
    <p class="sub" style="top:664px;color:#555">Lisis Pretium Nunc</p>
    <div class="rule" style="top:677px"></div>
    <div class="filters"><span class="on">All Items</span><span>Beverages</span><span>Starter</span><span>Meat</span><span>Vegetarian</span><span>Desserts</span></div>
    <div class="photo" style="left:53px;top:712px;width:157px;height:73px;background:linear-gradient(120deg,#c98a30,#7a4a18 45%,#d8b070)" role="img" aria-label="Fried pickles with dipping sauce"></div>
    <div class="photo" style="left:212px;top:712px;width:79px;height:73px;background:linear-gradient(150deg,#3a2a20,#b8a890 60%,#e8e0d0)" role="img" aria-label="Pulled pork sandwich on paper"></div>
    <div class="photo" style="left:293px;top:712px;width:79px;height:73px;background:linear-gradient(150deg,#2a3040,#8a4a30 55%,#c04040)" role="img" aria-label="Basket of ribs"></div>
    <div class="photo" style="left:53px;top:787px;width:78px;height:73px;background:linear-gradient(160deg,#5a3018,#a0502a 55%,#3a2a20)" role="img" aria-label="Sauce bottles on a counter"></div>
    <div class="photo" style="left:133px;top:787px;width:78px;height:73px;background:linear-gradient(160deg,#3a4050,#8a8a90 55%,#5a5f6a)" role="img" aria-label="Pitmaster standing in the restaurant"></div>
    <div class="photo" style="left:214px;top:787px;width:158px;height:73px;background:linear-gradient(110deg,#4a2a1a,#9a3a18 45%,#d06a28)" role="img" aria-label="Brisket with sweet potato fries"></div>
  </section>

  <section class="team">
    <h2 class="title" style="top:878px;font-size:12px">FOOD GALLERY</h2>
    <p class="sub" style="top:897px;color:#555">Lisis Pretium Nunc Elementum Ligula Lobortis Eget</p>
    <div class="rule" style="top:910px"></div>
    <div class="chef photo" style="left:56px;background:linear-gradient(160deg,#8a5a3a,#e8e4e0 60%,#bbb)" role="img" aria-label="Chef in white uniform"></div>
    <div class="chef photo" style="left:137px;background:linear-gradient(160deg,#e6e2dc,#c8c0b8 55%,#b04030)" role="img" aria-label="Chef holding a plated salad"></div>
    <div class="chef photo" style="left:218px;background:linear-gradient(160deg,#c8d0d8,#e8e6e2 55%,#a8a098)" role="img" aria-label="Smiling chef with arms folded"></div>
    <div class="chef photo" style="left:299px;background:linear-gradient(160deg,#5a4a40,#e4e0da 55%,#9a6a40)" role="img" aria-label="Chef garnishing a dish"></div>
    <div class="chef-cap" style="left:51px"><b>FUSCE SUSCIPIT</b><i>Malesuada Quisque</i><span>Pitmaster for twenty years, keeper<br>of the hickory fire.</span></div>
    <div class="chef-cap" style="left:132px"><b>FUSCE SUSCIPIT</b><i>Malesuada Quisque</i><span>Sides and salads made fresh<br>every single morning.</span></div>
    <div class="chef-cap" style="left:213px"><b>FUSCE SUSCIPIT</b><i>Malesuada Quisque</i><span>Head cook, rubs and sauces<br>from family recipes.</span></div>
    <div class="chef-cap" style="left:294px"><b>FUSCE SUSCIPIT</b><i>Malesuada Quisque</i><span>Pies, cobbler and banana<br>pudding baked daily.</span></div>
  </section>

  <section class="abs band" style="top:1051px;height:171px;background:linear-gradient(180deg,#0e0e0e,#1d1d1d 50%,#0c0c0c)">
    <h2 class="title" style="top:20px;font-size:12px">OUR SPECIAL OFFER</h2>
    <p class="sub" style="top:37px">Praesent Rutrum Pretium Urna</p>
    <div class="rule" style="top:50px"></div>
  </section>
  <div class="abs form-label">RESERVATIONS FORM</div>
  <div class="field" style="left:53px;top:1128px;width:157px">Full Name
    <svg width="5" height="5" viewBox="0 0 10 10"><circle cx="5" cy="3" r="2.4" fill="#fff"/><path d="M1 10c0-3 2-4.5 4-4.5S9 7 9 10z" fill="#fff"/></svg></div>
  <div class="field" style="left:215px;top:1128px;width:157px">Your Email id
    <svg width="5" height="5" viewBox="0 0 10 10"><rect x="0.5" y="2" width="9" height="6.5" fill="#fff"/><path d="M.5 2l4.5 4 4.5-4" stroke="#333" fill="none"/></svg></div>
  <div class="field" style="left:53px;top:1147px;width:157px">Enter Your Phone Number
    <svg width="5" height="5" viewBox="0 0 10 10"><path d="M2 1l2 2-1 1.5c.8 1.5 1.8 2.5 3.3 3.3L7.8 6.8l2 2L8.5 10C4 9.5.5 6 0 1.5z" fill="#fff"/></svg></div>
  <div class="field" style="left:215px;top:1147px;width:157px">2
    <svg width="4" height="7" viewBox="0 0 4 10"><rect width="4" height="10" fill="#ddd"/></svg></div>
  <div class="field" style="left:53px;top:1165px;width:157px">Pick a Date
    <svg width="5" height="5" viewBox="0 0 10 10"><rect x=".5" y="1.5" width="9" height="8" fill="#fff"/><rect x=".5" y="1.5" width="9" height="2" fill="#999"/></svg></div>
  <div class="field" style="left:215px;top:1165px;width:157px">Pick a Time
    <svg width="5" height="5" viewBox="0 0 10 10"><circle cx="5" cy="5" r="4.2" fill="none" stroke="#fff"/><path d="M5 2.5V5h2" stroke="#fff" fill="none"/></svg></div>
  <div class="abs res-note">Call ahead for large parties and we will save the best table</div>
  <div class="abs res-btn">MAKE RESERVATIONS</div>

  <section class="blog">
    <h2 class="title" style="top:1240px;font-size:12px">OUR BLOG</h2>
    <p class="sub" style="top:1259px;color:#555">Lisis Pretium Nunc</p>
    <div class="rule" style="top:1272px"></div>
    <div class="post-img photo" style="left:53px;background:linear-gradient(150deg,#2a2a2a,#8a6a58 55%,#d8d0c8)" role="img" aria-label="Ribs on a paper-lined tray"></div>
    <div class="post" style="left:133px"><h4>FUSCE SUSCIPIT DUNMORE</h4><div class="meta">◷ 20 Dec, 2016 &nbsp; ♡ 20 &nbsp; ✉ 30</div><p>Fresh from the pit this week: a new<br>brisket rub, sides we love, and how<br>we keep the hickory fire going all<br>night long for the lunch crowd.</p><div class="more">READ MORE...</div></div>
    <div class="post-img photo" style="left:215px;background:linear-gradient(150deg,#6a2a18,#e07040 55%,#f0c080)" role="img" aria-label="Iced fruit drinks on a table"></div>
    <div class="post" style="left:296px"><h4>FUSCE SUSCIPIT DUNMORE</h4><div class="meta">◷ 20 Dec, 2016 &nbsp; ♡ 20 &nbsp; ✉ 30</div><p>Summer coolers are back on the<br>menu with lemonade, sweet tea<br>and peach punch to pair with<br>your favourite plate of ribs.</p><div class="more">READ MORE...</div></div>
  </section>

  <footer>
    <div class="abs footer"></div>
    <div class="abs foot-brand">DUNMORE<br>SMOKE</div>
    <div class="abs foot-txt" style="left:53px;top:1428px;width:72px"><b>VESTIBULUM EUISMOD TORTOR</b><br>Southern barbecue smoked over<br>hickory every day, with sides and<br>pies made in house. Family owned<br>and proud to serve our town for<br>many years now.</div>
    <h5 style="left:140px">Working Hours</h5>
    <div class="abs foot-txt" style="left:140px;top:1417px;width:85px"><b>◷ Monday To Friday</b><br>&nbsp;&nbsp;&nbsp;8:00 am to 10:00 pm (Breakfast)<br>&nbsp;&nbsp;&nbsp;11:00am to 10:00pm (Lunch/Dinner)<br><br><b>◷ Saturday &amp; Sunday</b><br>&nbsp;&nbsp;&nbsp;10:00am to 11:00 pm (Breakfast)<br>&nbsp;&nbsp;&nbsp;11:00am to 12:00pm (Lunch/Dinner)</div>
    <h5 style="left:228px">RECENT WORK</h5>
    <div class="thumb photo" style="left:228px;top:1421px;background:#6a3a20" role="img" aria-label="Grilled meat"></div>
    <div class="thumb photo" style="left:246px;top:1421px;background:#3a4a6a" role="img" aria-label="Dining room"></div>
    <div class="thumb photo" style="left:264px;top:1421px;background:#8a5a30" role="img" aria-label="Sides plate"></div>
    <div class="thumb photo" style="left:282px;top:1421px;background:#4a5a70" role="img" aria-label="Restaurant counter"></div>
    <div class="thumb photo" style="left:228px;top:1438px;background:#a04a20" role="img" aria-label="Ribs"></div>
    <div class="thumb photo" style="left:246px;top:1438px;background:#5a3a30" role="img" aria-label="Brisket"></div>
    <div class="thumb photo" style="left:264px;top:1438px;background:#b06a30" role="img" aria-label="Fries"></div>
    <div class="thumb photo" style="left:282px;top:1438px;background:#4a3a3a" role="img" aria-label="Sauces"></div>
    <h5 style="left:312px">CONTACT US</h5>
    <div class="abs foot-txt" style="left:312px;top:1414px;width:70px"><b>⌖</b> 1420 Ridgeway Road, Suite 3<br>&nbsp;&nbsp;&nbsp;Ridgeway, Alabama<br><br><b>✆</b> 9863-555-0148<br><br><b>✉</b> info@dunmoresmokehouse.com</div>
    <div class="abs copy">© 2017 All Rights Reserved. dunmoresmokehouse.com</div>
  </footer>

</main>
</div>
</body>
</html>
```